Granite Ridge Holdings

I have a real estate investment business.

** I need editable vector files of the final design.

Industry/Entity Type

Real Estate

Contact Information for Business Card

I would like the card to be clear and direct with the company name and contact info. I would prefer not to have a design that is too busy (i.e., with excessive detail) in the business card.

Font styles to use
Sans Serif

Requirements
Must have
• My card must have the following information listed below:
• Company name: Grainite Ridge Holdings LLC
• My name: Daniel Vorsley
• Phone number: (555) 218-9067
• Email address: dtvorsley@mailbox-example.net
• Keywords: “Real Estate Investments”
Nice to have
• I would like to have a design that resembles the characteristics/uses of obsidian stone which resembles something related to strength and resilience. Perhaps something with sharp, sleek color transitions as well.

```html
<!DOCTYPE html>
<html lang="en">
<head>
<meta charset="utf-8">
<title>Grainite Ridge Holdings LLC – Business Card</title>
<link href="https://fonts.googleapis.com/css2?family=Urbanist:wght@300;700&display=swap" rel="stylesheet">
<style>
  :root {
    --page-bg: #8d8d8f;
    --card-bg: #000000;
    --ink: #ffffff;
    --tone-dark: #141416;
    --tone-mid: #333335;
  }
  html, body {
    margin: 0;
    width: 1200px;
    height: 1000px;
    overflow: hidden;
    background: var(--page-bg);
  }
  .card {
    position: absolute;
    left: 197px;
    top: 269px;
    width: 806px;
    height: 460px;
    background: var(--card-bg);
    overflow: hidden;
    font-family: "Urbanist", sans-serif;
    color: var(--ink);
  }
  .card__texture {
    position: absolute;
    left: 0;
    top: 0;
  }
  .card__name {
    position: absolute;
    left: 28px;
    top: 74px;
    margin: 0;
    font-size: 47px;
    font-weight: 700;
    line-height: 1;
  }
  .card__rule {
    position: absolute;
    left: 29px;
    top: 134px;
    width: 489px;
    height: 5px;
    background: var(--ink);
  }
  .card__company {
    position: absolute;
    left: 28px;
    top: 156px;
    margin: 0;
    font-size: 37px;
    font-weight: 700;
    line-height: 1;
  }
  .card__tagline {
    position: absolute;
    left: 28px;
    top: 198px;
    margin: 0;
    font-size: 25px;
    font-weight: 300;
    line-height: 1;
  }
  .contact {
    position: absolute;
    left: 29px;
    display: flex;
    align-items: center;
    gap: 8px;
    font-size: 25px;
    font-weight: 700;
    line-height: 1;
  }
  .contact--phone { top: 340px; }
  .contact--email { top: 391px; }
  .contact__icon { flex: none; fill: var(--ink); }
</style>
</head>
<body>
  <div class="card">
    <svg class="card__texture" width="806" height="460" viewBox="0 0 806 460" role="img" aria-label="Dark stone-toned area with a soft grey gradient">
      <defs>
        <linearGradient id="stoneTone" x1="0" y1="0" x2="1" y2="1">
          <stop offset="0" stop-color="var(--tone-dark)"/>
          <stop offset="1" stop-color="var(--tone-mid)"/>
        </linearGradient>
      </defs>
      <polygon fill="url(#stoneTone)" points="580,0 806,0 806,460 360,460"/>
    </svg>

    <h1 class="card__name">Daniel Vorsley</h1>
    <div class="card__rule"></div>
    <h2 class="card__company">Grainite Ridge Holdings LLC</h2>
    <p class="card__tagline">Real Estate Investments</p>

    <div class="contact contact--phone">
      <svg class="contact__icon" width="26" height="36" viewBox="0 0 26 36" aria-hidden="true">
        <path d="M5 2 L11 1 L13 10 L9 12 C8 16 8 20 9 24 L13 26 L11 35 L5 34 C0 26 0 10 5 2 Z"/>
      </svg>
      <span>(555) 218-9067</span>
    </div>

    <div class="contact contact--email">
      <svg class="contact__icon" width="32" height="22" viewBox="0 0 32 22" aria-hidden="true">
        <path d="M0 0 H32 V22 H0 Z M3 3 V19 L10 11 Z M29 3 L22 11 L29 19 Z M4 2 L16 13 L28 2 Z M5 20 H27 L20 13 L16 16.5 L12 13 Z" fill-rule="evenodd"/>
      </svg>
      <span>dtvorsley@mailbox-example.net</span>
    </div>
  </div>
</body>
</html>
```